Sandwich Menu Design for TV Display

I'm looking for an upscale elegant redesign of our deli sandwich menu. It will be displayed on a 4k tv. We are an upscale Butcher Shoppe with prepared meals, wine by the bottle, as well as deli sandwiches. I have a design we've used in the past but would like ideas on bringing this to a newer looking elegant design.

```html
<!DOCTYPE html>
<html lang="en">
<head>
<meta charset="utf-8">
<title>Deli Sandwiches Menu Board</title>
<link href="https://fonts.googleapis.com/css2?family=Montserrat:wght@700;800;900&family=Mulish:ital,wght@1,300;1,400&family=Oswald:wght@400;500&family=Pinyon+Script&display=swap" rel="stylesheet">
<style>
  :root {
    --backdrop: #8a8a8a;
    --cream: #f4ede7;
    --ink: #1d1b1c;
    --charcoal: #2b292a;
    --deli-red: #b3121c;
    --gold: #cdb47c;
    --ivory: #f2ecda;
    --ivory-soft: #e6dfcf;
    --white: #ffffff;
    --blush: #ece2e2;
  }
  * { margin: 0; padding: 0; box-sizing: border-box; }
  html, body { width: 1200px; height: 908px; overflow: hidden; }
  body { background: var(--backdrop); position: relative; font-family: "Mulish", sans-serif; }

  .menu-board {
    position: absolute; left: 30px; top: 133px;
    width: 1140px; height: 641px;
    background: linear-gradient(180deg, var(--cream) 0%, #f8f4ef 100%);
    overflow: hidden;
  }

  .side-photo {
    position: absolute; left: 0; top: 0; width: 228px; height: 641px;
    background: linear-gradient(180deg, #f3ebe2 0%, #ece1d3 45%, #e2d3bd 80%, #d9c6aa 100%);
  }

  .brand {
    position: absolute; left: 12px; top: 60px; width: 204px;
    display: flex; flex-direction: column; align-items: center;
  }
  .brand-name {
    display: flex; align-items: center; gap: 8px;
    font-family: "Oswald", sans-serif; font-weight: 500; color: var(--deli-red);
    font-size: 22px; line-height: 1.1; text-transform: uppercase; letter-spacing: 0.5px;
    text-align: center;
  }
  .brand-dot {
    width: 12px; height: 12px; border-radius: 50%; background: var(--deli-red); flex: none;
  }
  .brand-tagline {
    margin-top: 62px;
    font-family: "Oswald", sans-serif; font-weight: 400; color: var(--deli-red);
    font-size: 16px; letter-spacing: 0.2px;
  }

  .offer-box {
    position: absolute; left: 23px; top: 201px; width: 181px; height: 339px;
    background: var(--deli-red); color: var(--white);
    font-family: "Oswald", sans-serif; font-weight: 500; text-transform: uppercase;
    text-align: center; font-size: 19px; line-height: 20.5px;
    padding-top: 20px;
  }
  .offer-box .price { font-size: 30px; line-height: 28px; }
  .offer-box .divider {
    width: 112px; margin: 30px auto 28px; border-top: 2px dotted rgba(255,255,255,0.9);
  }

  .title {
    position: absolute; left: 228px; top: 31px;
    font-family: "Montserrat", sans-serif; font-weight: 900;
    font-size: 88px; line-height: 88px; letter-spacing: 1.5px;
    color: var(--ink); white-space: nowrap; z-index: 1;
  }

  .panel-dark {
    position: absolute; left: 228px; top: 105px; width: 456px; height: 536px;
    background: var(--charcoal); z-index: 2;
  }
  .panel-red {
    position: absolute; left: 684px; top: 105px; width: 456px; height: 447px;
    background: var(--deli-red); z-index: 2;
  }
  .panel-white {
    position: absolute; left: 684px; top: 552px; width: 456px; height: 89px;
    background: var(--white); z-index: 2;
    display: flex; align-items: center; justify-content: center;
  }
  .script-tagline {
    font-family: "Pinyon Script", cursive; color: var(--deli-red); font-size: 36px;
  }

  .item-list { position: absolute; top: 44px; left: 47px; width: 364px; list-style: none; }
  .item { margin-bottom: 11px; }
  .item-name {
    font-family: "Montserrat", sans-serif; font-weight: 800;
    font-size: 23px; line-height: 22px; letter-spacing: 0.6px; text-transform: uppercase;
  }
  .item-desc {
    font-style: italic; font-weight: 300; font-size: 15px; line-height: 14.3px;
    letter-spacing: 0.3px; text-align: justify; text-align-last: left;
  }

  .panel-dark .item-name { color: var(--ivory); }
  .panel-dark .item-desc { color: var(--ivory-soft); }
  .panel-dark .item.featured .item-name,
  .panel-dark .item.featured .item-desc { color: var(--gold); }
  .panel-red .item-name, .panel-red .item-desc { color: var(--white); }
  .panel-red .item.featured .item-name { color: var(--blush); }
</style>
</head>
<body>
  <main class="menu-board">
    <div class="side-photo" role="img" aria-label="Softly lit photo of a wine bottle and a plated sandwich"></div>

    <div class="brand">
      <p class="brand-name"><span class="brand-dot"></span>Carver &amp; Vine<br>Provisions</p>
      <p class="brand-tagline">Fine Cuts. Warm Hospitality.</p>
    </div>

    <aside class="offer-box">
      <p>All<br>made-to-order<br>sandwiches are<br><span class="price">$12.99</span> and<br>served with a<br>choice of chips</p>
      <div class="divider"></div>
      <p>Build your own<br>sandwich or<br>choose one of<br>our signature<br>sandwiches</p>
    </aside>

    <h1 class="title">DELI SANDWICHES</h1>

    <section class="panel-dark">
      <ul class="item-list">
        <li class="item featured"><h2 class="item-name">Brooklyn</h2><p class="item-desc">Prosciutto I Capicola I Genoa Salami I Provolone Cheese I Mayo I Lettuce I Tomato I Onion</p></li>
        <li class="item"><h2 class="item-name">Big Apple</h2><p class="item-desc">Roast Beef I Capicola I Turkey I Muenster Cheese I Mayo I Lettuce I Tomato I Onion</p></li>
        <li class="item"><h2 class="item-name">Italian</h2><p class="item-desc">Genoa Salami I Capicola I Provolone Cheese I Pepperoni I Mayo I Lettuce I Tomato I Onion</p></li>
        <li class="item"><h2 class="item-name">Verrazano</h2><p class="item-desc">Pastrami I Swiss Cheese I Rye Bread I Mayo I Lettuce I Tomato I Onion</p></li>
        <li class="item"><h2 class="item-name">Big B.L.T.</h2><p class="item-desc">Bacon I Lettuce I Tomato I Mayo</p></li>
        <li class="item"><h2 class="item-name">Chicken Salad</h2><p class="item-desc">House Chicken Salad with Cranberries I Lettuce I Tomato I Onion</p></li>
        <li class="item"><h2 class="item-name">Lady Liberty</h2><p class="item-desc">Turkey I Bacon I Avocado I American Cheese I Mayo I Lettuce I Tomato I Onion</p></li>
      </ul>
    </section>

    <section class="panel-red">
      <ul class="item-list">
        <li class="item"><h2 class="item-name">Cuban</h2><p class="item-desc">Capicolla I Roasted Pork I Swiss I Pickles I Mustard on Cuban Bread</p></li>
        <li class="item"><h2 class="item-name">Tampa</h2><p class="item-desc">Capicolla I Roasted Pork I Salami I Provolone I Pickles I Mustard on Cuban Bread</p></li>
        <li class="item"><h2 class="item-name">Rueben</h2><p class="item-desc">Corned Beef I Swiss Cheese I Sauerkraut I Thousand Island Dressing on Rye Bread</p></li>
        <li class="item"><h2 class="item-name">Wall Street Hog</h2><p class="item-desc">Slow Smoked Pulled Pork I Cole Slaw I Housemade BBQ Sauce</p></li>
        <li class="item featured"><h2 class="item-name">Brooklyn Baloney</h2><p class="item-desc">Fried Beef Bologna I Cheddar Cheese I Garlic Butter I Mayo I Lettuce I Tomato I Onion</p></li>
        <li class="item"><h2 class="item-name">Junior Wall Street</h2><p class="item-desc">Choice of Turkey &amp; American Cheese or Peanut Butter &amp; Jelly on a 4" hoagie</p></li>
      </ul>
    </section>

    <footer class="panel-white"><p class="script-tagline">Fine Cuts. Warm Hospitality.</p></footer>
  </main>
</body>
</html>
```